Pool Screen Enclosure Building a Career Boot Camp!

Looking to Host a Boot Camp for people looking for a career or looking to change careers. We Design, Manufacture and Install Custom Pool Screen Enclosures. We have a training program to allow Non Experienced motivated people the chance at a great career that will provide a great living for them and their family. This will be a paid boot camp, week long, we provide all the initial training for them to make a transition into our business. This will be 5 days of training with a guaranteed job to start the following Monday.... This is good for both someone with no construction experience or someone with construction experience that wants to upgrade their current job.
Paid Boot Camp
transition to a full time job with great pay
Benefits include Health Insurance, Dental and Vision, 401K, we provide the tools and training.

```html
<!DOCTYPE html>
<html lang="en">
<head>
<meta charset="utf-8">
<title>Pool Screen Enclosure Career Boot Camp</title>
<link rel="stylesheet" href="https://fonts.googleapis.com/css2?family=Outfit:wght@400;500;600;700;800;900&display=swap">
<style>
  :root{
    --green:#12953f;
    --green-bright:#5cc22e;
    --ink:#15181b;
    --paper:#ffffff;
    --stage:#e4e4e4;
    --white:#ffffff;
  }
  *{margin:0;padding:0;box-sizing:border-box}
  html,body{width:1200px;height:1200px;overflow:hidden;background:var(--stage)}
  body{font-family:"Outfit",sans-serif;color:var(--ink)}
  .flyer{position:absolute;left:150px;top:17px;width:900px;height:1166px;background:var(--paper)}
  .brand{position:absolute;left:62px;top:64px;display:flex;align-items:center;gap:10px}
  .brand-dot{width:26px;height:26px;border-radius:50%;background:var(--green-bright)}
  .brand-name{font-size:22px;font-weight:700;color:var(--green-bright);line-height:1}
  .brand-tag{position:absolute;left:98px;top:94px;font-size:10.5px;font-weight:400;color:var(--green-bright)}
  .tagline{position:absolute;right:58px;top:66px;font-size:20px;font-weight:800;letter-spacing:-.2px}
  .hero{position:absolute;left:52px;top:129px;width:790px;height:428px;border-radius:32px 0 32px 0;overflow:hidden;display:flex}
  .hero-panel{width:395px;height:100%;background:linear-gradient(160deg,#16a046,#0f8a3a);position:relative}
  .hero-photo{flex:1;background:linear-gradient(180deg,#c9d1da 0%,#8f9aa6 45%,#5f6b57 70%,#7fb0bd 100%)}
  .headline{position:absolute;left:43px;top:52px;color:var(--white);font-weight:800;text-transform:uppercase;line-height:.98}
  .headline .lead{font-size:39px;display:block;letter-spacing:-.3px}
  .headline .big{font-size:70px;display:block;color:var(--ink);font-weight:900;letter-spacing:-1.5px;margin-top:6px;line-height:.95}
  .headline .camp{font-size:45px;display:block;color:var(--ink);font-weight:900;letter-spacing:-1px}
  .hero-intro{position:absolute;left:43px;top:308px;width:320px;font-size:19.5px;font-weight:500;line-height:24px;color:var(--ink)}
  .work-photo{position:absolute;top:576px;width:192px;height:249px;border-radius:0 0 22px 0}
  .work-photo.one{left:52px;background:linear-gradient(180deg,#b9c4cf,#5c646b 60%,#9a9386)}
  .work-photo.two{left:253px;background:linear-gradient(180deg,#5d8ec9,#b7c9dc 55%,#c9bfae)}
  .about{position:absolute;left:486px;top:569px;width:356px;height:256px;background:var(--ink);border-radius:0 24px 24px 0;color:var(--white)}
  .about-title{position:absolute;left:-62px;top:102px;width:200px;transform:rotate(-90deg);font-size:41px;font-weight:700;color:var(--green);text-align:center;letter-spacing:-.5px}
  .about-text{position:absolute;left:83px;top:36px;width:262px;font-size:18px;line-height:21.2px;font-weight:400;white-space:nowrap}
  .paid{position:absolute;left:486px;top:839px;width:354px;height:70px;background:var(--green);border-radius:0 6px 6px 0;color:var(--white);font-size:28px;font-weight:800;line-height:29px;padding:7px 0 0 26px;text-transform:uppercase;letter-spacing:-.3px}
  .paid-text{position:absolute;left:486px;top:920px;width:360px;font-size:18px;line-height:21.2px;white-space:nowrap}
  .perks{position:absolute;left:56px;top:856px;list-style:none}
  .perks::before{content:"";position:absolute;left:15px;top:18px;height:152px;border-left:2px dotted var(--green)}
  .perks li{position:relative;height:38.3px;display:flex;align-items:center;gap:17px;font-size:18px;font-weight:600;white-space:nowrap}
  .perk-icon{width:30px;height:30px;border-radius:50%;background:var(--ink);border:2px solid #dcdcdc;display:flex;align-items:center;justify-content:center;position:relative;z-index:1}
  .perk-icon span{width:10px;height:11px;background:var(--white);border-radius:2px}
  .footer{position:absolute;left:52px;top:1073px;width:787px;height:54px;display:flex;color:var(--white)}
  .footer div{display:flex;align-items:center;gap:14px}
  .footer-phone{width:256px;background:var(--ink);padding-left:16px;font-size:27px;font-weight:600}
  .footer-address{width:266px;background:var(--green);padding-left:16px;font-size:16.5px;font-weight:600;line-height:19px;text-transform:uppercase}
  .footer-web{flex:1;background:var(--ink);padding-left:16px;font-size:18px;font-weight:600}
</style>
</head>
<body>
<main class="flyer">
  <div class="brand"><div class="brand-dot"></div><div class="brand-name">Harbor Screen Works</div></div>
  <div class="brand-tag">Outdoor rooms built to last</div>
  <div class="tagline">ENJOY THE LIFESTYLE OF FLORIDA LIVING</div>

  <section class="hero">
    <div class="hero-panel">
      <h1 class="headline">
        <span class="lead">Pool Screen<br>Enclosure<br>Building a</span>
        <span class="big">Career</span>
        <span class="camp">Boot Camp!</span>
      </h1>
      <p class="hero-intro">Looking to Host a Boot Camp for people looking for a career or looking to change careers.</p>
    </div>
    <div class="hero-photo" role="img" aria-label="Photo of a finished screened pool enclosure at dusk with lounge chairs beside the pool"></div>
  </section>

  <div class="work-photo one" role="img" aria-label="Photo of an installer on a ladder fitting screen panels inside an enclosure frame"></div>
  <div class="work-photo two" role="img" aria-label="Photo of two workers on a roof installing an enclosure frame under a blue sky"></div>

  <section class="about">
    <h2 class="about-title">ABOUT US</h2>
    <p class="about-text">We Design, Manufacture and<br>Install Custom Pool Screen<br>Enclosures. We have a<br>training program to allow<br>Non Experienced motivated<br>people the chance at a great<br>career that will provide a<br>great living for them and<br>their family.</p>
  </section>

  <div class="paid">This will be a paid<br>boot camp</div>
  <p class="paid-text">This will be 5 days of training with a<br>guaranteed job to start the following<br>Monday.. This is good for both someone with<br>no construction experience or someone<br>with construction experience that wants to<br>upgrade their current job.</p>

  <ul class="perks">
    <li><div class="perk-icon"><span></span></div>Paid Boot Camp</li>
    <li><div class="perk-icon"><span></span></div>Transition to a full time job with great pay</li>
    <li><div class="perk-icon"><span></span></div>Benefits include Health Insurance</li>
    <li><div class="perk-icon"><span></span></div>Dental and Vision</li>
    <li><div class="perk-icon"><span></span></div>401K, we provide the tools and training</li>
  </ul>

  <footer class="footer">
    <div class="footer-phone">
      <svg width="24" height="24" viewBox="0 0 24 24" fill="none" stroke="currentColor" stroke-width="2.2" stroke-linecap="round" stroke-linejoin="round"><path d="M5 3h4l2 5-2.5 1.5a11 11 0 0 0 6 6L16 13l5 2v4a2 2 0 0 1-2 2A16 16 0 0 1 3 5a2 2 0 0 1 2-2z"/></svg>
      555-014-2287
    </div>
    <div class="footer-address">
      <svg width="22" height="26" viewBox="0 0 22 26" fill="none" stroke="var(--ink)" stroke-width="2.4"><path d="M11 24s8-8 8-14a8 8 0 0 0-16 0c0 6 8 14 8 14z"/><circle cx="11" cy="10" r="3"/></svg>
      <span>218 Palm Grove Avenue<br>Sunport, FL 30000</span>
    </div>
    <div class="footer-web">
      <svg width="24" height="24" viewBox="0 0 24 24" fill="none" stroke="currentColor" stroke-width="1.8"><circle cx="12" cy="12" r="10"/><ellipse cx="12" cy="12" rx="4.5" ry="10"/><path d="M2 12h20M4 7h16M4 17h16"/></svg>
      harborscreenworks.com
    </div>
  </footer>
</main>
</body>
</html>
```